Bref créative |
Birch Hydraulic | ||
Use same font as used in my logo | ||
Cutting-Edge Corporate Professional Simple |
Paul Destry | ||
Owner | ||
4637 Heron Ridge Lane Clarkston MI 48351 |
destry.paul@mailvane.net | ||

```html
<!DOCTYPE html>
<html lang="en">
<head>
<meta charset="utf-8">
<title>Birch Hydraulic — Business Card</title>
<link href="https://fonts.googleapis.com/css2?family=Arimo:wght@400;700&display=swap" rel="stylesheet">
<style>
  :root {
    --backdrop: #d4d4d4;
    --card: #ffffff;
    --card-edge: #9a9a9a;
    --ink: #222222;
    --green-dark: #1f8a3c;
    --green-mid: #2ea44a;
    --green-light: #a6cf3a;
  }
  html, body {
    margin: 0;
    padding: 0;
    width: 1200px;
    height: 938px;
    overflow: hidden;
    background: var(--backdrop);
    font-family: "Arimo", sans-serif;
  }
  .card {
    position: absolute;
    left: 145px;
    top: 191px;
    width: 989px;
    height: 615px;
    background: var(--card);
    border: 1px solid var(--card-edge);
    overflow: hidden;
  }
  .card-swooshes {
    position: absolute;
    inset: 0;
    width: 100%;
    height: 100%;
  }
  .contact-person {
    position: absolute;
    left: 79px;
    top: 22px;
    color: var(--ink);
  }
  .person-name {
    margin: 0;
    font-size: 35px;
    font-weight: 400;
    line-height: 40px;
  }
  .person-role, .person-cell {
    margin: 0;
    font-size: 25px;
    line-height: 29px;
  }
  .contact-office {
    position: absolute;
    left: 79px;
    top: 388px;
    color: var(--ink);
    font-size: 25px;
    line-height: 27px;
  }
  .contact-office p { margin: 0; }
  .brand {
    position: absolute;
    left: 615px;
    top: 235px;
    width: 300px;
    display: flex;
    align-items: center;
    gap: 16px;
  }
  .brand-mark {
    width: 46px;
    height: 46px;
    background: var(--green-dark);
    flex: none;
  }
  .brand-name {
    font-size: 44px;
    font-weight: 700;
    line-height: 48px;
    color: var(--green-dark);
  }
</style>
</head>
<body>
  <div class="card">
    <svg class="card-swooshes" viewBox="0 0 989 615" preserveAspectRatio="none" aria-hidden="true">
      <path d="M0 175 C 250 90, 520 250, 989 30 L 989 55 C 520 265, 250 110, 0 190 Z" fill="var(--green-light)"/>
      <path d="M0 205 C 260 120, 540 290, 989 45 L 989 80 C 540 320, 260 150, 0 230 Z" fill="var(--green-mid)"/>
      <path d="M0 270 C 260 320, 520 330, 989 540 L 989 575 C 520 360, 260 340, 0 292 Z" fill="var(--green-dark)"/>
      <path d="M0 300 C 280 355, 560 370, 989 600 L 989 615 L 960 615 C 560 390, 280 370, 0 315 Z" fill="var(--green-light)"/>
    </svg>

    <div class="contact-person">
      <h1 class="person-name">Paul Destry</h1>
      <p class="person-role">Owner</p>
      <p class="person-cell">Cell : 586-555-0142</p>
    </div>

    <div class="contact-office">
      <p>4637 Heron Ridge Lane</p>
      <p>Clarkston MI 48351</p>
      <p>Ph: 586-555-0187</p>
      <p>Fax : 586-555-0142</p>
      <p>Email : destry.paul@mailvane.net</p>
    </div>

    <div class="brand">
      <span class="brand-mark"></span>
      <span class="brand-name">Birch Hydraulic</span>
    </div>
  </div>
</body>
</html>
```